Magazine advertisement

I need a company advertisement for magazine prints. I need to be able to scale it to different sizes if need be. I need it to showcase our brand, VornaDrive have our phone number 582.463.9047 our contact email address sales@vornadrive.net and web address www.vornadrive.net

Target Market(s)

automotive / tractor pulling

Industry/Entity Type

automotive / racing

Colors
EB3D1F
EC4F4E
F09395
F8D3D4
FCEDEE

Requirements
Must have
• our logo, our color scheme (pantone red 1795, white, black, silver

```html
<!DOCTYPE html>
<html lang="en">
<head>
<meta charset="utf-8">
<title>VornaDrive – Custom Turbochargers</title>
<link rel="stylesheet" href="https://fonts.googleapis.com/css2?family=Bebas+Neue&family=Montserrat:wght@600;700&display=swap">
<style>
  :root {
    --red: #e6393b;
    --red-deep: #b5161b;
    --black: #111111;
    --white: #ffffff;
    --silver: #8c8d91;
    --metal-light: #e4e4e4;
    --metal-dark: #8a8a8a;
    --dot-tint: rgba(248, 211, 212, 0.35);
  }
  * { margin: 0; padding: 0; box-sizing: border-box; }
  html, body { width: 899px; height: 1200px; overflow: hidden; background: var(--white); }
  .ad {
    position: relative;
    width: 899px;
    height: 1200px;
    overflow: hidden;
    background: var(--white);
    font-family: "Montserrat", Arial, sans-serif;
  }
  .ad-shapes { position: absolute; inset: 0; }
  .brand {
    position: absolute;
    top: 118px;
    left: 0;
    width: 934px;
    text-align: center;
    font-family: "Montserrat", Arial, sans-serif;
    font-weight: 700;
    font-size: 40px;
    letter-spacing: 2px;
    color: var(--red);
    text-transform: uppercase;
  }
  .headline {
    position: absolute;
    left: 0;
    width: 934px;
    text-align: center;
    font-family: "Bebas Neue", Impact, sans-serif;
    color: var(--red);
    line-height: 1;
  }
  .headline-main { top: 176px; font-size: 176px; letter-spacing: 2px; }
  .headline-sub { top: 322px; font-size: 82px; letter-spacing: 1px; }
  .tagline {
    position: absolute;
    top: 408px;
    left: 0;
    width: 946px;
    text-align: center;
    font-weight: 600;
    font-size: 27px;
    color: var(--black);
  }
  .product-shot {
    position: absolute;
    left: 241px;
    top: 456px;
    width: 480px;
    height: 540px;
  }
  .contact {
    position: absolute;
    color: var(--white);
    font-weight: 700;
  }
  .contact-call { left: 52px; top: 1054px; }
  .call-label { font-size: 24px; letter-spacing: 0.5px; }
  .call-number { display: flex; align-items: center; gap: 14px; margin-top: 4px; font-size: 35px; }
  .contact-links { left: 478px; top: 1064px; width: 360px; font-size: 23px; }
  .contact-row { display: flex; align-items: center; justify-content: space-between; height: 40px; }
  .contact-row svg { flex: none; }
</style>
</head>
<body>
<main class="ad">
  <svg class="ad-shapes" width="899" height="1200" viewBox="0 0 899 1200" aria-hidden="true">
    <defs>
      <linearGradient id="base-fade" x1="0" y1="0" x2="0" y2="1">
        <stop offset="0.72" stop-color="var(--red)"/>
        <stop offset="1" stop-color="var(--red-deep)"/>
      </linearGradient>
    </defs>
    <!-- side accent strip -->
    <polygon points="0,0 37,0 37,312 0,361" fill="var(--red)"/>
    <!-- lower panel with black edge -->
    <polygon points="0,593 454,738 899,588 899,600 454,751 0,605" fill="var(--black)"/>
    <polygon points="0,605 454,751 899,600 899,1200 0,1200" fill="url(#base-fade)"/>
    <!-- slanted bar accents -->
    <g fill="var(--red)">
      <polygon points="120,445 146,430 174,474 148,489"/>
      <polygon points="152,426 176,412 204,456 178,471"/>
      <polygon points="736,354 757,356 754,412 733,409"/>
      <polygon points="761,356 781,358 779,414 758,412"/>
      <polygon points="785,358 806,360 803,416 782,414"/>
    </g>
    <!-- product shadow -->
    <ellipse cx="470" cy="1000" rx="170" ry="14" fill="var(--red-deep)" opacity="0.6"/>
  </svg>

  <svg class="ad-shapes" width="899" height="1200" viewBox="0 0 899 1200">
    <rect x="82" y="743" width="28" height="198" fill="var(--dot-tint)" role="img" aria-label="Decorative dot grid"/>
    <rect x="781" y="827" width="118" height="30" fill="var(--dot-tint)" role="img" aria-label="Decorative dot grid"/>
  </svg>

  <div class="brand">VornaDrive</div>
  <div class="headline headline-main">Custom</div>
  <div class="headline headline-sub">Turbochargers</div>
  <div class="tagline">FOR EXTREME MOTORSPORTS</div>

  <svg class="product-shot" viewBox="0 0 480 540" role="img" aria-label="Photo of a billet turbocharger with machined compressor wheel">
    <defs>
      <radialGradient id="metal" cx="0.4" cy="0.4" r="0.7">
        <stop offset="0" stop-color="var(--metal-light)"/>
        <stop offset="1" stop-color="var(--metal-dark)"/>
      </radialGradient>
    </defs>
    <ellipse cx="240" cy="290" rx="235" ry="245" fill="url(#metal)"/>
  </svg>

  <div class="contact contact-call">
    <div class="call-label">CALL NOW</div>
    <div class="call-number">
      <svg width="40" height="40" viewBox="0 0 40 40" aria-hidden="true">
        <circle cx="20" cy="20" r="20" fill="var(--white)"/>
        <path d="M13 11c1-1 2.5-1 3.2 0l2 3c.6.9.4 2-.4 2.6l-1.3 1c1 2.4 2.8 4.3 5.2 5.4l1-1.3c.6-.8 1.8-1 2.6-.4l3 2c1 .7 1 2.2 0 3.2l-1.5 1.5c-1.3 1.3-3.3 1.6-5 .8-4.8-2.3-8.6-6.1-10.9-10.9-.8-1.7-.5-3.7.8-5z" fill="var(--red)"/>
      </svg>
      <span>582.463.9047</span>
    </div>
  </div>

  <div class="contact contact-links">
    <div class="contact-row">
      <svg width="30" height="20" viewBox="0 0 30 20" aria-hidden="true">
        <rect x="1" y="1" width="28" height="18" fill="var(--white)"/>
        <path d="M1 1l14 10L29 1M1 19l10-9M29 19l-10-9" stroke="var(--red)" stroke-width="2" fill="none"/>
      </svg>
      <span>SALES@VORNADRIVE.NET</span>
    </div>
    <div class="contact-row">
      <svg width="26" height="26" viewBox="0 0 26 26" aria-hidden="true" fill="none" stroke="var(--white)" stroke-width="2">
        <circle cx="13" cy="13" r="11"/>
        <ellipse cx="13" cy="13" rx="5" ry="11"/>
        <path d="M2 13h22M4 7h18M4 19h18"/>
      </svg>
      <span>WWW.VORNADRIVE.NET</span>
    </div>
  </div>
</main>
</body>
</html>
```